Business Cards for a Luggage Service (Repair, Sales, Warranty Etc.) Company
Belmora Baggage Services
Professional
Gregory Talvane
Owner
2418 Quillon Ave. Suite 320 Atlanta, GA 30987
Info@BelmoraBaggageServices.example
www.BelmoraBaggageServices.example
The logo was made for my sign. So it's a bit big.
tkalvin tkalvin
Our company is a luggage service company. We repair luggage, provide warranty related services, and sell new luggage. We are located within 1 mile of Atlanta's Pembrook Dallow International Airport (worlds busiest airport). We specialize in flight crew luggage repair and services.

```html
<!DOCTYPE html>
<html lang="en">
<head>
<meta charset="utf-8">
<title>Belmora Baggage Services – Business Cards</title>
<link href="https://fonts.googleapis.com/css2?family=Montserrat:wght@400;500;700&display=swap" rel="stylesheet">
<style>
  :root {
    --stage: #d9d9d9;
    --card-white: #ffffff;
    --ink: #1c1c1c;
    --night: #111111;
    --brand-red: #e0262c;
    --soft-red: #f0585c;
    --light-text: #f2f2f2;
    --muted: #9a9a9a;
  }
  * { box-sizing: border-box; margin: 0; padding: 0; }
  html, body { width: 1200px; height: 818px; overflow: hidden; }
  body {
    background: var(--stage);
    font-family: "Montserrat", sans-serif;
    position: relative;
  }
  .card {
    position: absolute;
    width: 560px;
    height: 320px;
    border-radius: 14px;
    overflow: hidden;
    background: var(--card-white);
    box-shadow: 0 8px 24px rgba(0,0,0,0.18);
  }
  .card--back { left: 140px; top: 110px; }
  .card--front { left: 500px; top: 390px; }

  .brand {
    position: absolute;
    display: flex;
    align-items: center;
    gap: 12px;
  }
  .brand__mark {
    width: 34px; height: 34px;
    background: var(--brand-red);
    border-radius: 3px;
    flex: none;
  }
  .brand__name {
    font-weight: 700;
    color: var(--ink);
    line-height: 1.05;
    letter-spacing: 0.5px;
    text-transform: uppercase;
  }
  .brand__tagline {
    position: absolute;
    font-size: 7px;
    letter-spacing: 2.2px;
    color: var(--muted);
    text-transform: uppercase;
  }
  .card--back .brand { left: 70px; top: 118px; }
  .card--back .brand__name { font-size: 22px; }
  .card--back .brand__tagline { left: 116px; top: 178px; }

  .card--front .brand { left: 38px; top: 36px; }
  .card--front .brand__mark { width: 28px; height: 28px; }
  .card--front .brand__name { font-size: 16px; }
  .card--front .brand__tagline { left: 78px; top: 84px; font-size: 6px; }

  .wave { position: absolute; inset: 0; width: 100%; height: 100%; }

  .person {
    position: absolute;
    left: 38px; top: 226px;
    color: var(--light-text);
  }
  .person__name { font-size: 17px; font-weight: 500; letter-spacing: 1px; text-transform: uppercase; }
  .person__role { font-size: 8px; letter-spacing: 1.6px; margin-top: 4px; color: #cfcfcf; text-transform: uppercase; }

  .contact {
    position: absolute;
    right: 28px; top: 176px;
    list-style: none;
    color: var(--light-text);
    font-size: 8.5px;
    text-align: right;
  }
  .contact__item {
    display: flex; justify-content: flex-end; align-items: center;
    gap: 7px; line-height: 1.35; margin-bottom: 5px;
  }
  .contact__icon { width: 10px; height: 10px; flex: none; fill: var(--light-text); }
  .contact__gap { margin-top: 8px; }
</style>
</head>
<body>

<section class="card card--back" aria-label="Card back">
  <div class="brand">
    <span class="brand__mark"></span>
    <span class="brand__name">Belmora<br>Baggage Services</span>
  </div>
  <p class="brand__tagline">Repair · Warranty · Sales</p>
</section>

<section class="card card--front" aria-label="Card front">
  <svg class="wave" viewBox="0 0 560 320" preserveAspectRatio="none" aria-hidden="true">
    <path d="M0 150 C140 120 250 88 370 116 C460 136 520 124 560 106" fill="none" stroke="var(--soft-red)" stroke-width="3"/>
    <path d="M0 162 C140 134 260 100 375 128 C465 148 522 136 560 118" fill="none" stroke="var(--brand-red)" stroke-width="7"/>
    <path d="M0 176 C150 150 265 114 380 142 C468 162 524 150 560 132" fill="none" stroke="var(--brand-red)" stroke-width="5"/>
    <path d="M0 192 C150 166 270 128 385 156 C470 176 525 164 560 146 L560 320 L0 320 Z" fill="var(--night)"/>
  </svg>

  <div class="brand">
    <span class="brand__mark"></span>
    <span class="brand__name">Belmora<br>Baggage Services</span>
  </div>
  <p class="brand__tagline">Repair · Warranty · Sales</p>

  <div class="person">
    <p class="person__name">Gregory Talvane</p>
    <p class="person__role">Owner</p>
  </div>

  <ul class="contact">
    <li class="contact__item"><span>2418 Quillon Ave. Suite 320<br>Atlanta, GA 30987</span>
      <svg class="contact__icon" viewBox="0 0 10 10"><path d="M5 0a3.5 3.5 0 0 0-3.5 3.5C1.5 6 5 10 5 10s3.5-4 3.5-6.5A3.5 3.5 0 0 0 5 0zm0 5a1.5 1.5 0 1 1 0-3 1.5 1.5 0 0 1 0 3z"/></svg></li>
    <li class="contact__item contact__gap"><span>404 555 0142</span>
      <svg class="contact__icon" viewBox="0 0 10 10"><path d="M2 0l2 2.5-1 1.2a6 6 0 0 0 3.3 3.3l1.2-1L10 8l-1.5 2C4 9.5.5 6 0 1.5z"/></svg></li>
    <li class="contact__item"><span>404 555 0187</span>
      <svg class="contact__icon" viewBox="0 0 10 10"><path d="M2 0l2 2.5-1 1.2a6 6 0 0 0 3.3 3.3l1.2-1L10 8l-1.5 2C4 9.5.5 6 0 1.5z"/></svg></li>
    <li class="contact__item"><span>404 555 0199</span>
      <svg class="contact__icon" viewBox="0 0 10 10"><path d="M2 0l2 2.5-1 1.2a6 6 0 0 0 3.3 3.3l1.2-1L10 8l-1.5 2C4 9.5.5 6 0 1.5z"/></svg></li>
    <li class="contact__item"><span>Info@BelmoraBaggageServices.example</span>
      <svg class="contact__icon" viewBox="0 0 10 10"><path d="M0 2h10v6H0z M0 2l5 3.5L10 2" fill="none" stroke="var(--light-text)" stroke-width="1"/></svg></li>
    <li class="contact__item"><span>www.BelmoraBaggageServices.example</span>
      <svg class="contact__icon" viewBox="0 0 10 10"><circle cx="5" cy="5" r="4.4" fill="none" stroke="var(--light-text)" stroke-width="1"/><path d="M0.6 5h8.8M5 0.6c-2.4 2.6-2.4 6.2 0 8.8M5 0.6c2.4 2.6 2.4 6.2 0 8.8" fill="none" stroke="var(--light-text)" stroke-width="0.8"/></svg></li>
  </ul>
</section>

</body>
</html>
```